Tilda Tinkerwire, An IT Company Has New Logo, Need Fresh Business Cards

IT company is called Tilda Tinkerwire and is displayed nicely with the new logo from here on pitchloft. Would like a fresh business card look that encompasses the idea that we want clients to Cherish Every Gadget. I love the use of circuitry with hearts as endpoints and x's and o's. It needs to have room for my certification logos of which there are 4 and a BRJ Alumni log. I am attaching my current card to illustrate how it has always captured attention, but that was in the early stages of business when I was doing more residential work. I am focused on businesses now, so a level of professionalism is necessary. I would also like the card to lend itself well to additional stationary, email signature, ticketing template for my workboard, etc. For the time being, I need the card for an upcoming conference so that work will come later. Color scheme should be that of the new logo. Thank you and I look forward to the designs.

Target Market(s)

Businesses looking for IT services.

Industry/Entity Type

Information Technology

Contact Information for Business Card

See above

Requirements
Must have
• New logo colors and a warm feel. Possibly a tad feminine as I am female, but appealing to males.
Nice to have
• I would like techy, but no too much so. I like friendly and connecting feels. People LOVED my old card and called me because it gave them a warm feeling.

```html
<!DOCTYPE html>
<html lang="en">
<head>
<meta charset="utf-8">
<title>Tilda Tinkerwire — Business Card</title>
<link rel="stylesheet" href="https://fonts.googleapis.com/css2?family=Mulish:wght@400;500&family=Roboto:wght@400;500;700&display=swap">
<style>
  :root {
    --page: #ecebe8;
    --card-white: #ffffff;
    --card-blue: #86c8e6;
    --brand-blue: #7cc4e4;
    --brand-pink: #e59ac4;
    --brand-green: #b9d86a;
    --brand-lilac: #c9a3d1;
    --ink: #4a4a4a;
    --ink-soft: #5a5a5a;
    --white: #ffffff;
  }
  * { box-sizing: border-box; margin: 0; padding: 0; }
  html, body { width: 1200px; height: 1200px; overflow: hidden; }
  body {
    background: var(--page);
    font-family: "Roboto", Arial, sans-serif;
    position: relative;
  }
  .card {
    position: absolute;
    left: 213px;
    width: 773px;
    height: 440px;
    overflow: hidden;
    box-shadow: 0 3px 10px rgba(0,0,0,.18);
  }
  .card--front { top: 151px; background: var(--card-white); }
  .card--back { top: 633px; background: var(--card-blue); color: var(--white); text-align: center; }

  .feature-art {
    position: absolute;
    left: 432px; top: 112px;
    width: 341px; height: 328px;
    border-radius: 50% 0 0 50% / 50% 0 0 50%;
    background:
      radial-gradient(circle at 30% 35%, rgba(229,154,196,.35), transparent 55%),
      radial-gradient(circle at 70% 30%, rgba(185,216,106,.35), transparent 55%),
      radial-gradient(circle at 55% 70%, rgba(124,196,228,.38), transparent 60%),
      radial-gradient(circle at 85% 65%, rgba(201,163,209,.3), transparent 55%);
  }
  .backdrop-art {
    position: absolute;
    left: 340px; top: 0;
    width: 433px; height: 440px;
    background: linear-gradient(100deg, rgba(255,255,255,0) 0%, rgba(255,255,255,.14) 45%, rgba(255,255,255,.2) 100%);
  }

  .brand { position: absolute; text-align: center; }
  .card--front .brand { left: 40px; width: 300px; top: 60px; }
  .brand__dot {
    display: block; margin: 0 auto 34px;
    width: 72px; height: 72px; border-radius: 50%;
    background: var(--brand-pink);
  }
  .brand__name {
    font-family: "Mulish", Arial, sans-serif;
    font-weight: 400;
    font-size: 31px;
    letter-spacing: -0.3px;
    color: var(--brand-blue);
    line-height: 1;
  }
  .brand__tagline {
    font-family: "Mulish", Arial, sans-serif;
    font-size: 10.5px;
    letter-spacing: 3.2px;
    text-transform: uppercase;
    color: var(--brand-pink);
    margin-top: 7px;
  }

  .person { position: absolute; left: 42px; top: 248px; }
  .person__name { font-size: 28px; font-weight: 500; color: var(--ink); }
  .person__title { font-size: 19px; color: var(--brand-blue); margin-top: 6px; }

  .contact { position: absolute; left: 42px; top: 328px; list-style: none; }
  .contact li {
    display: flex; align-items: center; gap: 8px;
    font-size: 18px; color: var(--ink-soft); height: 27px;
  }
  .contact li.contact__phone { font-weight: 700; }
  .contact svg { width: 16px; height: 16px; flex: none; }

  .card--back .brand { left: 0; right: 0; top: 126px; }
  .card--back .brand__dot { background: var(--white); width: 100px; height: 100px; margin-bottom: 48px; }
  .card--back .brand__name { color: var(--white); font-size: 48px; }
  .card--back .brand__tagline { color: var(--white); font-size: 14px; letter-spacing: 5px; margin-top: 6px; }
  .services {
    position: absolute; left: 0; right: 0; top: 380px;
    font-size: 22px; font-weight: 500; letter-spacing: .2px;
  }
  .services span { margin: 0 10px; font-weight: 400; }
</style>
</head>
<body>
  <section class="card card--front">
    <div class="feature-art" role="img" aria-label="Large pastel brand decoration area"></div>

    <div class="brand">
      <span class="brand__dot"></span>
      <div class="brand__name">Tilda Tinkerwire</div>
      <div class="brand__tagline">× Cherish Every Gadget ×</div>
    </div>

    <div class="person">
      <div class="person__name">Marcus Hale</div>
      <div class="person__title">President &amp; CEO</div>
    </div>

    <ul class="contact">
      <li class="contact__phone">
        <svg viewBox="0 0 16 16" fill="none" stroke="#e59ac4" stroke-width="1.3"><path d="M3 2h3l1 3-2 1.2a8 8 0 0 0 4.8 4.8L11 9l3 1v3a1 1 0 0 1-1 1A12 12 0 0 1 2 3a1 1 0 0 1 1-1z"/></svg>
        555-014-2283
      </li>
      <li>
        <svg viewBox="0 0 16 16" fill="none" stroke="#e59ac4" stroke-width="1.3"><rect x="1.5" y="3.5" width="13" height="9"/><path d="M1.5 3.5 8 9l6.5-5.5"/></svg>
        hello@tilda-tinkerwire.example
      </li>
      <li>
        <svg viewBox="0 0 16 16" fill="none" stroke="#c9a3d1" stroke-width="1.2"><circle cx="8" cy="8" r="6.5"/><ellipse cx="8" cy="8" rx="3" ry="6.5"/><path d="M1.5 8h13M2.5 5h11M2.5 11h11"/></svg>
        www.tilda-tinkerwire.example
      </li>
    </ul>
  </section>

  <section class="card card--back">
    <div class="backdrop-art" role="img" aria-label="Faint brand decoration area"></div>
    <div class="brand">
      <span class="brand__dot"></span>
      <div class="brand__name">Tilda Tinkerwire</div>
      <div class="brand__tagline">× Cherish Every Gadget ×</div>
    </div>
    <div class="services">Desktops<span>|</span>Laptops<span>|</span>Tablets</div>
  </section>
</body>
</html>
```